business card, stationary, email signature, envelopes
Bold Grins, PLLC
business card, stationary, email signature, envelopes - Medical
Creative Brief
Bright & Fun-filled
714 Harwick Ave Dover, NH 03827
boldgrinspllc@quorvamail.com
BoldGrinsPLLC.com

```html
<!DOCTYPE html>
<html lang="en">
<head>
<meta charset="utf-8">
<title>Bold Grins, PLLC — Business Card</title>
<link rel="stylesheet" href="https://fonts.googleapis.com/css2?family=Roboto:wght@400;500;700&display=swap">
<style>
  :root {
    --stage: #e9e6e1;
    --card-blue: #3d5f95;
    --card-blue-dark: #33507f;
    --brand-blue: #2f86c6;
    --accent-pink: #e2306f;
    --paper-top: #ffffff;
    --paper-bottom: #e4e4e4;
    --ink: #3c3c3c;
    --ink-soft: #6a6a6a;
    --white: #ffffff;
  }
  * { box-sizing: border-box; margin: 0; padding: 0; }
  html, body {
    width: 1200px; height: 958px; overflow: hidden;
    background: var(--stage);
    font-family: "Roboto", Arial, sans-serif;
  }
  .stage { position: relative; width: 1200px; height: 958px; }
  .card {
    position: absolute; top: 159px;
    width: 400px; height: 640px;
    box-shadow: 0 10px 28px rgba(0,0,0,0.22);
    overflow: hidden;
  }
  /* Back of card */
  .card-back {
    left: 150px;
    background: linear-gradient(160deg, var(--card-blue), var(--card-blue-dark));
  }
  .web-bar {
    position: absolute; left: 150px; right: 0; top: 300px; height: 44px;
    background: linear-gradient(180deg, #ffffff, #dcdcdc);
    display: flex; align-items: center; padding-left: 20px;
    font-size: 15px; color: var(--ink-soft); letter-spacing: 0.2px;
  }
  /* Front of card */
  .card-front {
    left: 650px;
    background: linear-gradient(170deg, var(--paper-top) 30%, var(--paper-bottom));
  }
  .brand {
    position: absolute; top: 150px; left: 0; right: 0;
    display: flex; justify-content: center; align-items: center; gap: 12px;
  }
  .brand-name {
    font-size: 46px; font-weight: 500; color: var(--brand-blue); letter-spacing: -1px;
  }
  .brand-dot {
    width: 14px; height: 14px; border-radius: 50%; background: var(--accent-pink);
  }
  .person { position: absolute; top: 350px; left: 0; right: 0; }
  .person-bar {
    position: absolute; left: 0; top: 0; width: 50px; height: 40px;
    background: var(--accent-pink);
  }
  .person-name {
    margin-left: 66px; font-size: 18px; font-weight: 500; color: var(--ink);
    letter-spacing: 0.5px; line-height: 20px;
  }
  .person-title {
    margin-left: 66px; font-size: 12px; color: var(--ink-soft); line-height: 18px;
  }
  .contact { position: absolute; top: 440px; left: 0; right: 0; }
  .contact-rail {
    position: absolute; left: 0; top: 0; width: 40px; height: 170px;
    background: var(--card-blue);
  }
  .contact-list { list-style: none; }
  .contact-item {
    position: relative; height: 34px;
    display: flex; align-items: center;
    padding-left: 66px; font-size: 13px; color: var(--ink);
  }
  .contact-item svg {
    position: absolute; left: 12px; top: 9px; width: 16px; height: 16px;
  }
</style>
</head>
<body>
<main class="stage">
  <section class="card card-back" aria-label="Business card back">
    <div class="web-bar">BoldGrinsPLLC.com</div>
  </section>

  <section class="card card-front" aria-label="Business card front">
    <div class="brand">
      <span class="brand-name">Bold Grins</span>
      <span class="brand-dot"></span>
    </div>

    <div class="person">
      <div class="person-bar"></div>
      <p class="person-name">ELLIOT MARSH</p>
      <p class="person-title">Managing Director</p>
    </div>

    <div class="contact">
      <div class="contact-rail"></div>
      <ul class="contact-list">
        <li class="contact-item">
          <svg viewBox="0 0 16 16" aria-hidden="true"><path fill="#fff" d="M4 1h3l1 4-2 1c1 2 2 3 4 4l1-2 4 1v3c0 1-1 2-2 2C6 14 2 10 2 3c0-1 1-2 2-2z"/></svg>
          012 555 0142
        </li>
        <li class="contact-item">
          <svg viewBox="0 0 16 16" aria-hidden="true"><rect x="4" y="1" width="8" height="14" rx="1.5" fill="#fff"/><rect x="5.5" y="3" width="5" height="8" fill="#3d5f95"/></svg>
          012 555 0143
        </li>
        <li class="contact-item">
          <svg viewBox="0 0 16 16" aria-hidden="true"><rect x="3" y="6" width="10" height="7" fill="#fff"/><rect x="5" y="2" width="6" height="4" fill="#fff"/></svg>
          012 555 0144
        </li>
        <li class="contact-item">
          <svg viewBox="0 0 16 16" aria-hidden="true"><rect x="1" y="3" width="14" height="10" fill="#fff"/><path d="M1 3l7 6 7-6" fill="none" stroke="#3d5f95" stroke-width="1.3"/></svg>
          boldgrinspllc@quorvamail.com
        </li>
        <li class="contact-item">
          <svg viewBox="0 0 16 16" aria-hidden="true"><path fill="#fff" d="M8 1a5 5 0 0 1 5 5c0 4-5 9-5 9S3 10 3 6a5 5 0 0 1 5-5z"/><circle cx="8" cy="6" r="2" fill="#3d5f95"/></svg>
          714 Harwick Ave Dover, NH 03827
        </li>
      </ul>
    </div>
  </section>
</main>
</body>
</html>
```